Vantry Forge (IT/Network Services)

Vantry Forge, LLC provides technology services to small and medium businesses. Essentially, anytime you've every thought your business might need an "IT guy" to handle something you could instead call us to handle it. Basically, you can outsource your IT needs to us.

This is a brand new company and so we'll need a brand new website. I'd like to use WordPress to handle the site since that will make things easier for me to maintain in the long run.

The site should include a, more-or-less, static front page with the dynamic data occurring on pages linked from a navigational area.

I have a logo already designed that I would like to see used in the design. The one with "white" in the title is the official logo, just added some other versions for your perusal.

Color queues from the logo but feel free to add other colors where applicable.

The site should feel somewhat corporate but with a "younger" slant (something a 25-35 year old would enjoy).

Pages (either to be added initially or by me after design completion):
"About" section - includes company history, business philosophy, etc.
"Services" section - service options, service approach, service specifics
"Testimonials" section - (eventually)
"News" section - (eventually) industry news, company news, events, blog
Contact Links

Websites to view:
The two largest local competitors:
http://www.harbelmsystemsinc.example/
http://www.qubrix.example/
Other local competitors:
http://www.plkllc.example/
http://www.merowaygroup.example/

Other info you might find useful:
Domain: vfllc.example
Address:
517 Calder Ln W
Suite 742B
Nashville, TN 37288
Phone: 615-555-0187
Emails available for use/display:
info@vfllc.example
sales@vfllc.example

Target Market(s)

Our target clients are mainly small businesses (25 or less computer users) which means we're looking at a lot of start-ups or younger companies. We'll be interacting with many entrepreneurs and young business owners.

Requirements
Must have
• Need full WP theme (not a mockup)

```html
<!DOCTYPE html>
<html lang="en">
<head>
<meta charset="utf-8">
<title>Vantry Forge — IT &amp; Network Services</title>
<link href="https://fonts.googleapis.com/css2?family=Open+Sans:wght@400;600&display=swap" rel="stylesheet">
<style>
:root{
  --orange:#f39200;
  --orange-dark:#e08400;
  --grey-text:#777;
  --body-text:#555;
  --dark:#222;
  --frame:#6e6e6e;
  --panel:#f6f6f6;
  --rule:#bbb;
  --title-red:#8b0c0c;
}
*{margin:0;padding:0;box-sizing:border-box}
html,body{width:1200px;height:1067px;overflow:hidden}
body{position:relative;font-family:Arial,Helvetica,sans-serif;
  background:linear-gradient(#000 0,#1a1a1a 90px,#4a4c4f 400px,#7b7e82 1067px);}
.abs{position:absolute}
.page{left:139px;top:9px;width:920px;height:963px;background:#fff;border-radius:4px;
  box-shadow:0 0 6px rgba(0,0,0,.5)}
.header{left:0;top:0;width:920px;height:135px;border-radius:4px 4px 0 0;
  background:linear-gradient(#f8f8f8,#f2f2f2);border-bottom:1px solid #e6e6e6}
.brand{left:26px;top:26px;display:flex;align-items:center;gap:16px}
.brand-mark{width:82px;height:82px;border-radius:50%;border:12px solid var(--orange)}
.brand-name{font-family:'Open Sans',sans-serif;font-weight:600;font-size:40px;color:var(--grey-text);letter-spacing:1px}
.search{left:666px;top:24px;width:241px;height:27px;border:1px solid #aaa;border-radius:14px;
  background:linear-gradient(#eee,#fafafa);font-size:11px;color:#888;padding:7px 0 0 26px}
.search svg{position:absolute;right:12px;top:5px}
.phone{left:684px;top:62px;display:flex;align-items:center;gap:10px;color:var(--orange);font-size:18px}
.phone-icon{width:30px;height:26px;border-radius:4px;background:linear-gradient(#ddd,#bbb);display:flex;align-items:center;justify-content:center}
.nav{top:104px;left:403px;height:24px;font-size:13px;color:#333}
.nav a{position:absolute;top:0;line-height:24px;text-decoration:none;color:#333;white-space:nowrap}
.nav .active{background:var(--orange);color:#fff;border-radius:8px;width:72px;text-align:center}
.slider{left:17px;top:143px;width:892px;height:334px}
.slider-shadow{left:20px;top:330px;width:630px;height:30px;border-radius:50%;
  background:radial-gradient(ellipse at top,rgba(0,0,0,.22),rgba(0,0,0,0) 70%)}
.slide-photo{left:14px;top:28px;width:532px;height:292px;
  background:linear-gradient(120deg,#cfeefa 0%,#4fc0e6 35%,#1693c4 60%,#a9def2 100%)}
.slide-text{left:546px;top:28px;width:335px;height:292px;background:#efefef}
.slide-title{left:577px;top:92px;font-size:18px;color:var(--title-red);letter-spacing:-.3px}
.slide-copy{left:577px;top:150px;width:300px;font-size:12.5px;line-height:20px;color:#222}
.arrow{width:20px;height:20px;border-radius:50%;background:#eee;border:1px solid #999;display:flex;align-items:center;justify-content:center}
.dots{left:478px;top:313px;display:flex;gap:4px}
.dots span{width:9px;height:9px;border-radius:50%;background:#888;border:1px solid #ccc}
.dots .on{background:var(--orange)}
.box{left:17px;width:230px;background:linear-gradient(#fff,var(--panel));border-bottom:8px solid var(--orange);border-radius:4px}
.box-head{height:29px;background:var(--orange);border-radius:4px 4px 0 0;color:#222;font-size:14px;padding:8px 0 0 26px}
.item{margin:0 8px;padding:10px 8px 6px;border-bottom:1px dotted #999;font-size:10.5px;line-height:15px;color:#999}
.item:last-of-type{border-bottom:0}
.item .date{color:#555;margin-bottom:5px}
.more{text-align:right;font-size:10.5px;color:#222;padding:0 9px 4px}
.testi{display:flex;gap:8px}
.avatar{width:44px;height:52px;flex:none;border-radius:3px;background:linear-gradient(#eee,#d8d8d8)}
.welcome{left:278px;top:527px}
.welcome h1{font-family:'Open Sans',sans-serif;font-weight:400;font-size:21px;color:var(--dark);
  padding-bottom:5px;border-bottom:1px dotted #555;width:226px}
.intro{left:279px;top:572px;width:612px;font-size:11.5px;line-height:20px;color:var(--body-text)}
.col h2{font-family:'Open Sans',sans-serif;font-weight:400;font-size:16px;color:var(--dark);margin:0 0 13px 12px}
.col .img{width:253px;height:101px;border:1px solid #ddd;background:linear-gradient(#fff,#eef3f7)}
.col p{margin:29px 0 0 14px;width:225px;font-size:10.5px;line-height:17px;color:#444}
.col .read{display:block;margin:10px 0 0 14px;font-size:10.5px;color:var(--orange);text-decoration:none}
.footer-label{left:153px;top:992px;font-size:14px;color:#ddd}
.news-input{left:148px;top:1021px;width:172px;height:28px;border-radius:3px;background:linear-gradient(#ddd,#fff)}
.news-go{left:294px;top:1021px;width:26px;height:28px;background:var(--orange);border-radius:0 3px 3px 0;font-size:11px;color:#222;text-align:center;line-height:28px}
.legal{left:520px;top:996px;width:280px;text-align:center;font-size:10.5px;color:#f2f2f2}
.legal a{color:#f2f2f2;text-decoration:none}
.legal .sep{margin:0 5px}
.legal p{margin-top:12px}
.social{left:916px;top:1014px;display:flex;gap:8px}
.social span{width:23px;height:21px;border-radius:3px;background:#4a8fd0;border:1px solid #ddd}
.social span:last-child{background:var(--orange)}
</style>
</head>
<body>
<div class="abs page">
  <header class="abs header">
    <div class="abs brand"><span class="brand-mark"></span><span class="brand-name">VANTRY FORGE</span></div>
    <div class="abs search">Search
      <svg width="18" height="18" viewBox="0 0 18 18"><circle cx="7" cy="7" r="5" fill="none" stroke="#777" stroke-width="1.6"/><path d="M11 11l5 5" stroke="#777" stroke-width="2.4"/></svg>
    </div>
    <div class="abs phone"><span class="phone-icon">
      <svg width="16" height="16" viewBox="0 0 16 16"><path d="M3 1c-2 2-2 6 2 10s8 4 10 2l-3-3-2 1c-2-1-3-2-4-4l1-2z" fill="#fff"/></svg></span>236 555 0142</div>
    <nav class="abs nav">
      <a class="active" style="left:0">Home</a>
      <a style="left:83px">Services</a>
      <a style="left:162px">Benefits</a>
      <a style="left:238px">Careers</a>
      <a style="left:311px">Newsroom</a>
      <a style="left:399px">Blog</a>
      <a style="left:454px">Contact</a>
    </nav>
  </header>

  <section class="abs slider">
    <div class="abs slider-shadow"></div>
    <svg class="abs" style="left:0;top:0" width="892" height="334" viewBox="0 0 892 334">
      <path d="M0 38 Q446 -20 892 38 V334 H0 Z" fill="var(--frame)"/>
      <path d="M4 44 Q446 -10 888 44" fill="none" stroke="#aaa" stroke-width="2"/>
    </svg>
    <div class="abs slide-photo" role="img" aria-label="Blue-toned photo of a computer keyboard with a world map and cable"></div>
    <div class="abs slide-text"></div>
    <div class="abs slide-title">TECHNOLOGY</div>
    <p class="abs slide-copy">Lorem ipsum dolor sit amet, consectetuer adipiscing elit, sed diam nonummy nibh euismod tincidunt ut laoreet dolore magna aliquam erat volutpat. Lorem ipsum dolor sit amet, consectetuer adipiscing elit, sed diam nonummy nibh euismod tincidunt.</p>
    <div class="abs arrow" style="left:6px;top:176px"><svg width="8" height="10"><path d="M6 1L2 5l4 4" stroke="#333" stroke-width="2" fill="none"/></svg></div>
    <div class="abs arrow" style="left:866px;top:176px"><svg width="8" height="10"><path d="M2 1l4 4-4 4" stroke="#333" stroke-width="2" fill="none"/></svg></div>
    <div class="abs dots"><span></span><span></span><span></span><span class="on"></span></div>
  </section>

  <aside class="abs box" style="top:501px;height:212px">
    <div class="box-head">LATEST NEWS</div>
    <div class="item"><div class="date">May 23, 2012</div>Nunc varius facilisis eros. Sed erat. In in velit quis arcu orne laoreet. Curabitur adipiscing luctus massa.</div>
    <div class="item"><div class="date">May 23, 2012</div>Nunc varius facilisis eros. Sed erat. In in velit quis arcu orne laoreet. Curabitur adipiscing luctus massa.</div>
    <div class="more">View More &gt;&gt;</div>
  </aside>

  <aside class="abs box" style="top:730px;height:218px">
    <div class="box-head">TESTIMONIALS</div>
    <div class="item testi"><div class="avatar" role="img" aria-label="Portrait of a client"></div><div><div class="date">May 23, 2012</div>Nunc varius facilisis eros. Sed erat. In in velit quis arcu orne laoreet.</div></div>
    <div class="item testi"><div class="avatar" role="img" aria-label="Portrait of a client"></div><div><div class="date">May 23, 2012</div>Nunc varius facilisis eros. Sed erat. In in velit quis arcu orne laoreet.</div></div>
    <div class="more">View More &gt;&gt;</div>
  </aside>

  <div class="abs welcome"><h1>Welcome to Our Site</h1></div>
  <p class="abs intro">Nunc varius facilisis eros. Sed erat. In in velit quis arcu ornare laoreet. Curabitur adipiscing luctus massa.Integer ut purus ac commodo Nunc varius facilisis eros. Sed erat. Nunc varius facilisis eros. Sed erat. In in velit quis arcu ornare laoreet. Curabitur adipiscing luctus massa.Integer ut purus ac commodo Nunc varius facilisis eros. Sed erat.</p>

  <section class="abs col" style="left:274px;top:657px">
    <h2>People</h2>
    <div class="img" role="img" aria-label="Illustration of colourful figures standing around a globe"></div>
    <p>Nunc varius facilisis eros. Sed erat. In in velit quis arcu ornare laoreet. Curabitur adipiscing luctus massa.Integer ut purus ac commodo Nunc varius facilisis eros.</p>
    <a class="read" href="#">Read More</a>
  </section>
  <section class="abs col" style="left:607px;top:657px">
    <h2>Perspective</h2>
    <div class="img" role="img" aria-label="Illustration of puzzle pieces with an email symbol"></div>
    <p>Nunc varius facilisis eros. Sed erat. In in velit quis arcu ornare laoreet. Curabitur adipiscing luctus massa.Integer ut purus ac commodo Nunc varius facilisis eros.</p>
    <a class="read" href="#">Read More</a>
  </section>
</div>

<footer>
  <div class="abs footer-label">Sign up to our newsletter!</div>
  <div class="abs news-input"></div>
  <div class="abs news-go">GO</div>
  <div class="abs legal">
    <a href="#">Privacy &amp; Legal</a><span class="sep">|</span><a href="#">Site Map</a><span class="sep">|</span><a href="#">Contact Us</a>
    <p>© 2012 Vantry Forge. All rights reserved</p>
  </div>
  <div class="abs social"><span></span><span></span><span></span><span></span><span></span></div>
</footer>
</body>
</html>
```